This is for a book cover design (front and back) and I need it to match my branding guidelines which I have attached below. I have also attached other books to show you what I'm looking for.

This book is about "A new way to make money online" which I believe is the best way to get to 7 figures FAST. So For the book I have a book example to give you all an example of what I am looking for but it still needs to be about digital online money and digital marketing.

The Book Title: The Golden Ladder Blueprint Codex
The Book Subtitle: Discover How To Sell Your Front End High Ticket Offers With No Sales Team, No VLS, No Phone Calls and Without Having A Huge Social Media Presence!

for the book could we go in the direction of having my face in the background and having it be like im the mastermind behind this revolutionary new way to make money. I included an image below to give you what the mind map could look like but you see how you have take the latest version we are almost there but not quite yet.
So in the middle of the mind map it would be a dollar sign $. The other pieces of the puzzle (or you could test one version out as puzzle pieces with the words on it below: So let's have two different versions - one with the mind map and one being puzzle pieces with the Center puzzle piece being $.
VIP Day
Challenges
Advertising
Identifying The BIG Problem
Webinars
Organic Reach
Trust Building
Value
Influencer Marketing
Gamification
Objection Handling
Artificial Intelligence
Applications
Financing
Email Marketing
Backends
Marketing Psychology
Sales
High Ticket Offers
Empathy Maps
List Building
Upsells
Customer Avatars
Podcasts
Webinars
Content Distribution
Customer Service
Merchant Processors
Systems
Sales
Still keeping the same look etc but testing out puzzle pieces with my face being the puzzle. Just thinking of something different and unique for my first book

• Puzzle Pieces & Mind Maps
• Utilize My Color Schemes

```html
<!DOCTYPE html>
<html lang="en">
<head>
<meta charset="utf-8">
<title>The Golden Ladder Blueprint Codex — Book Cover</title>
<link href="https://fonts.googleapis.com/css2?family=Oswald:wght@600;700&family=Montserrat:wght@600;700&family=Kaushan+Script&display=swap" rel="stylesheet">
<style>
  :root {
    --sky-top: #0c5377;
    --sky-mid: #08344f;
    --sky-deep: #03141f;
    --sky-low: #072b44;
    --brand-blue: #00aeef;
    --paper-white: #ececec;
    --rule-blue: #bfe6f7;
    --bill-light: #c3d3d2;
    --bill-mid: #9fb5b6;
    --bill-shadow: #6f8c92;
  }
  * { margin: 0; padding: 0; box-sizing: border-box; }
  html, body { width: 750px; height: 1200px; overflow: hidden; background: var(--sky-deep); }
  .cover {
    position: relative;
    width: 750px;
    height: 1200px;
    overflow: hidden;
    background:
      radial-gradient(ellipse 70% 30% at 45% 10%, rgba(18, 96, 138, 0.75), transparent 70%),
      radial-gradient(ellipse 60% 25% at 85% 55%, rgba(12, 70, 105, 0.55), transparent 70%),
      radial-gradient(ellipse 55% 20% at 15% 45%, rgba(1, 10, 18, 0.7), transparent 70%),
      linear-gradient(180deg, var(--sky-top) 0%, var(--sky-mid) 38%, var(--sky-deep) 62%, var(--sky-low) 82%, var(--sky-deep) 100%);
  }
  .cover-art {
    position: absolute;
    left: 78px;
    top: 135px;
    width: 637px;
    height: 295px;
    border-radius: 18px;
    background: linear-gradient(160deg, var(--bill-light) 0%, var(--bill-mid) 55%, var(--bill-shadow) 100%);
    opacity: 0.85;
  }
  .title-block {
    position: absolute;
    left: 0;
    top: 470px;
    width: 750px;
    height: 470px;
  }
  .title-article { font-family: 'Kaushan Script', cursive; fill: var(--paper-white); }
  .title-main { font-family: 'Oswald', sans-serif; font-weight: 700; fill: var(--brand-blue); }
  .title-tail { font-family: 'Oswald', sans-serif; font-weight: 700; fill: var(--paper-white); }
  .title-rule {
    position: absolute;
    left: 88px;
    top: 945px;
    width: 575px;
    height: 3px;
    background: var(--rule-blue);
  }
  .subtitle {
    position: absolute;
    left: 0;
    top: 955px;
    width: 750px;
    height: 90px;
  }
  .subtitle-line {
    font-family: 'Montserrat', sans-serif;
    font-weight: 600;
    font-size: 19px;
    fill: var(--paper-white);
  }
  .author-band {
    position: absolute;
    left: 3px;
    top: 1111px;
    width: 744px;
    height: 71px;
    background: var(--brand-blue);
  }
  .author-name { font-family: 'Montserrat', sans-serif; font-weight: 700; fill: var(--paper-white); }
</style>
</head>
<body>
  <main class="cover">
    <div class="cover-art" role="img" aria-label="Jigsaw puzzle pieces of a hundred-dollar banknote scattered and floating, with the main assembled section at upper left"></div>

    <svg class="title-block" viewBox="0 470 750 470" aria-label="The Golden Ladder Blueprint Codex">
      <text class="title-article" x="171" y="538" font-size="70">The</text>
      <text class="title-main" x="89" y="697" font-size="182" textLength="572" lengthAdjust="spacingAndGlyphs">GOLDEN</text>
      <text class="title-main" x="87" y="863" font-size="190" textLength="576" lengthAdjust="spacingAndGlyphs">LADDER</text>
      <text class="title-tail" x="87" y="928" font-size="66" textLength="576" lengthAdjust="spacingAndGlyphs">BLUEPRINT CODEX</text>
    </svg>

    <div class="title-rule"></div>

    <svg class="subtitle" viewBox="0 955 750 90" aria-label="Discover how to sell your front high end ticket offers with no sales team, no VLS, no phone calls and without having a huge social media presence!">
      <text class="subtitle-line" x="102" y="984" textLength="535" lengthAdjust="spacingAndGlyphs">DISCOVER HOW TO SELL YOUR FRONT HIGH END TICKET</text>
      <text class="subtitle-line" x="96" y="1009" textLength="552" lengthAdjust="spacingAndGlyphs">OFFERS WITH NO SALES TEAM, NO VLS, NO PHONE CALLS</text>
      <text class="subtitle-line" x="92" y="1034" textLength="568" lengthAdjust="spacingAndGlyphs">AND WITHOUT HAVING A HUGE SOCIAL MEDIA PRESENCE!</text>
    </svg>

    <svg class="author-band" viewBox="0 0 744 71">
      <text class="author-name" x="372" y="58" font-size="62" text-anchor="middle" textLength="436" lengthAdjust="spacingAndGlyphs">DORIAN WELLS</text>
    </svg>
  </main>
</body>
</html>
```